Facebook Header Design Project.

I'm supplying white and colored logos. The Facebook page already exists. URL = https://www.pagebook.example/lumocrest.design The design should not be based on what's already there. Consider mobile implications of the design. This Design will form the designs of other social media headers. LumoCrest is a web design | digital marketing company.

Target Market(s)

People interested in web design | digital marketing services.

Industry/Entity Type

LumoCrest is a web design | digital marketing company. That should be clear in the design.

Colors
0054AA
0677BA
7BADD7
CADEEF
E8F1F8

Requirements
Must have
• Logo. Use Facebook header image dimension.
Nice to have
• Use a color scheme like the logo and feel free to add a color or two from the other side of the color whee.

```html
<!DOCTYPE html>
<html lang="en">
<head>
<meta charset="utf-8">
<title>LumoCrest – Page Header</title>
<link rel="stylesheet" href="https://fonts.googleapis.com/css2?family=Barlow+Semi+Condensed:wght@300;600&family=Poppins:wght@400;600;700&display=swap">
<style>
  :root {
    --navy: #0054AA;
    --ocean: #0677BA;
    --sky: #7BADD7;
    --mist: #CADEEF;
    --frost: #E8F1F8;
    --white: #ffffff;
    --stage: #e5e5e5;
  }
  * { box-sizing: border-box; margin: 0; padding: 0; }
  html, body { width: 1200px; height: 826px; overflow: hidden; background: var(--stage); }
  .canvas { position: relative; width: 1200px; height: 826px; }
  .cover {
    position: absolute; left: 0; top: 185px;
    width: 1200px; height: 456px; overflow: hidden;
    background: var(--white);
  }
  .cover-art { position: absolute; inset: 0; width: 100%; height: 100%; }
  .cover-copy { position: absolute; left: 152px; top: 0; color: var(--white); }
  .brand {
    position: absolute; top: 104px; left: 0;
    font-family: "Poppins", sans-serif; font-weight: 600;
    font-size: 30px; letter-spacing: 0.5px; color: var(--white);
    white-space: nowrap;
  }
  .headline {
    position: absolute; top: 170px; left: 0; white-space: nowrap;
    font-family: "Barlow Semi Condensed", sans-serif;
    font-size: 46px; line-height: 44px; letter-spacing: 0.3px;
  }
  .headline strong { display: block; font-weight: 600; }
  .headline span { display: block; font-weight: 300; }
  .intro {
    position: absolute; top: 268px; left: 0; width: 360px;
    font-family: "Poppins", sans-serif; font-size: 12.5px; line-height: 16px;
    color: var(--mist);
  }
  .intro b { color: var(--white); font-weight: 700; }
  .cta {
    position: absolute; top: 332px; left: 0;
    display: flex; height: 32px; width: 271px;
    border: 2px solid var(--white); border-radius: 5px; overflow: hidden;
    font-family: "Poppins", sans-serif; white-space: nowrap;
  }
  .cta-label {
    background: var(--white); color: var(--navy);
    font-size: 11.5px; font-weight: 600; letter-spacing: 0.3px;
    padding: 0 10px; display: flex; align-items: center;
  }
  .cta-url {
    flex: 1; color: var(--white); font-size: 13px;
    display: flex; align-items: center; justify-content: center;
  }
  .cta-url b { font-weight: 700; }
</style>
</head>
<body>
<main class="canvas">
  <section class="cover" aria-label="LumoCrest page header">
    <svg class="cover-art" viewBox="0 0 1200 456" xmlns="http://www.w3.org/2000/svg">
      <defs>
        <linearGradient id="panelFill" x1="0" y1="0" x2="1" y2="0">
          <stop offset="0" stop-color="#0054AA"/>
          <stop offset="0.6" stop-color="#0067B4"/>
          <stop offset="1" stop-color="#0677BA"/>
        </linearGradient>
        <linearGradient id="photoTone" x1="0" y1="0" x2="0" y2="1">
          <stop offset="0" stop-color="#3f6f9f"/>
          <stop offset="0.5" stop-color="#3d6a99"/>
          <stop offset="1" stop-color="#5d8fc0"/>
        </linearGradient>
      </defs>
      <!-- base panel -->
      <path class="panel" d="M0 0 H990 L740 456 H0 Z" fill="url(#panelFill)"/>
      <!-- soft arcs -->
      <g class="panel-arcs" fill="none" stroke="#ffffff" stroke-opacity="0.12" stroke-width="1.5">
        <path d="M108 0 C92 150 92 300 108 456"/>
        <path d="M225 0 C205 150 205 300 225 456"/>
        <path d="M370 0 C330 150 330 300 355 456"/>
        <path d="M500 0 C430 140 420 320 470 456"/>
      </g>
      <!-- framing blob -->
      <path class="frame-blob" fill="#0054AA"
        d="M663 0 H990 C1050 30 1095 70 1108 150 C1118 240 1092 360 1030 456 H600 C565 400 537 320 537 240 C537 150 590 60 663 0 Z"/>
      <!-- photo -->
      <path role="img" aria-label="Photo: smiling man working on a laptop" fill="url(#photoTone)"
        d="M805 18 Q823 8 841 18 L1006 120 Q1018 128 1018 142 L1018 330 Q1018 344 1006 351 L836 444 Q822 452 806 444 L641 352 Q629 345 629 331 L629 143 Q629 129 641 121 Z"/>
      <!-- accent arc -->
      <path class="accent-arc" d="M620 296 C622 335 640 365 680 389" fill="none" stroke="#0677BA" stroke-width="14"/>
      <!-- edge line -->
      <path class="edge-line" d="M1175 5 C1215 90 1222 330 1180 456" fill="none" stroke="#7BADD7" stroke-width="2"/>
    </svg>

    <div class="cover-copy">
      <p class="brand">LumoCrest</p>
      <h1 class="headline"><strong>DIGITAL MARKETING</strong><span>AGENCY</span></h1>
      <p class="intro">LumoCrest provides <b>Web Design</b> and <b>Development</b>, Search Engine Optimization, <b>Graphic Design</b>, and <b>Digital Marketing Services</b>.</p>
      <p class="cta"><span class="cta-label">LEARN MORE</span><span class="cta-url">www.<b>LumoCrest</b>.example</span></p>
    </div>
  </section>
</main>
</body>
</html>
```